20€ Frühlings-Rabatt: Spare jetzt bei Deinem Wettbewerb mit dem Gutscheincode: Mai24
ansprechende Grafik für Leistungserstellungsprozess (Wertstrom) eines Holzbauunternehmens - Infografiken
Zielgruppe
Wir sind ein Holzbauunternehmen mit knapp 100 Mitarbeitern. Unsere Zielgruppen sind öffentliche, gwerbliche und private Bauherren.
Internetseite: lindtal-holzhaus.de
Aufgabenstellung
Der Prozess vom Bauwunsch unserer Kunden bis zur letzten Mängelabnahme soll anschaulich dargestellt werden. Dazu soll aus den bereits vorhandenen, verschiedenen grafischen Darstellungen unseres Leistungserstellungsprozesses (d.h. unseres Wertstromes) eine ansprechende Grafik entwickelt werden. Siehe dazu den Entwurf als Handskizze in elliptischer Form.
Ebenso ist eine Orientierung an unserem Firmenlogo wünschenswert.
Siehe: www.lindtal-holzhaus.de
Die Grafik dient zur Erklärung, Erläuterung unserer wesentlichen Prozess-Schritte für folgende Zielgruppen:
Kunden, Besuchergruppen, vorhandene Mitarbeiter (interne Schulungen), neue Mitarbeiter (Schulungen zur Einarbeitung), für externen Partner (Kommunikation)
Das Grafik soll zur Auflockerung mit passenden, leicht verständlichen, jedoch nicht zu vielen, grafischen Elementen angereichert werden.
Die Grafik soll in einer späteren Ausbaustufe auf eigenen Layern zusätzliche Elemente darstellen (z.B. die Teams, die vorhandenen Softwarewerkzeuge oder die verwendeten Dokumente) darstellen.
Als Grafiksoftware sind CorelDraw und Indesign im Betrieb vorhanden. Vorzugsweise soll die Grafik in diesen Formaten zur Verfügung gestellt werden können.

```html
<!DOCTYPE html>
<html lang="de">
<head>
<meta charset="utf-8">
<title>Lindtal Holzhaus – Wertstrom</title>
<link href="https://fonts.googleapis.com/css2?family=Jost:wght@400;500;700&display=swap" rel="stylesheet">
<style>
:root{
  --bg:#ffffff;
  --bar-top:#b9b9b9;
  --bar-bottom:#9b9b9b;
  --bar-text:#ffffff;
  --green:#3c9d2b;
  --dot-light:#7fd04a;
  --dot-dark:#2f9a22;
  --blue-top:#1271c4;
  --blue-bottom:#0a58a8;
  --red-top:#e3091b;
  --red-bottom:#c1121f;
  --rule:#e4e4e4;
  --brand:#1a1a1a;
  --brand-accent:#d9161f;
}
*{box-sizing:border-box;margin:0;padding:0}
html,body{width:1200px;height:1001px;overflow:hidden;background:var(--bg)}
body{position:relative;font-family:"Jost",sans-serif}
.flow{position:absolute;left:0;width:1200px;height:380px}
.flow--main{top:0}
.flow--alt{top:565px}
.step{position:absolute;height:30px;background:linear-gradient(var(--bar-top),var(--bar-bottom));color:var(--bar-text);font-size:8.4px;line-height:1.25;display:flex;align-items:center;justify-content:center;text-align:center;white-space:nowrap}
.step--fwd{padding-right:16px}
.step--back{padding-left:16px}
.step--bottom{top:315px}
.step--top{top:65px}
.step .chev{position:absolute;width:9px;height:9px;top:10.5px}
.step .chev--end{right:8px}
.step .chev--start{left:7px}
.step .two{display:flex;flex-direction:column;align-items:center}
.step .two span:first-child{border-bottom:1px solid rgba(255,255,255,.45);padding:0 4px}
.dot{position:absolute;width:17px;height:17px;border-radius:50%;background:radial-gradient(circle at 45% 35%,var(--dot-light),var(--dot-dark));transform:translate(-50%,-50%)}
.label{position:absolute;width:90px;transform:translateX(-50%);text-align:center;color:var(--green);font-size:8px;line-height:1.2;white-space:nowrap}
.label--aside{transform:none;left:945px;width:90px;text-align:right}
.ok{position:absolute;width:35px;height:35px;transform:translate(-50%,-50%);border-radius:50%;background:radial-gradient(circle at 45% 35%,#55c23a,#2b9420)}
.ok svg{width:35px;height:35px;display:block}
.actor{position:absolute;top:170px;width:69px;height:69px;color:#fff;display:flex;flex-direction:column;align-items:center;justify-content:flex-end;padding-bottom:4px}
.actor--customer{left:119px;background:linear-gradient(var(--blue-top),var(--blue-bottom))}
.actor--supplier{left:1029px;background:linear-gradient(var(--blue-top),var(--blue-bottom))}
.flow--alt .actor--supplier{background:linear-gradient(var(--red-top),var(--red-bottom))}
.actor .name{font-weight:500;white-space:nowrap}
.actor--customer .name{font-size:12.5px}
.actor--supplier .name{font-size:8.6px;margin-top:4px}
.actor svg{display:block}
.brand{position:absolute;top:0;left:0;width:1200px}
.brand .rule{position:absolute;top:484px;left:15px;width:1170px;height:1px;background:var(--rule)}
.brand .mark{position:absolute;top:466px;left:505px;width:190px;height:36px;background:var(--bg);display:flex;align-items:center;justify-content:center;gap:8px}
.brand .square{width:12px;height:12px;background:var(--brand-accent)}
.brand .name{font-size:16px;font-weight:700;color:var(--brand);letter-spacing:.5px;white-space:nowrap}
</style>
</head>
<body>

<section class="flow flow--main">
  <div class="step step--top step--fwd" style="left:119px;width:99px">Marketing<svg class="chev chev--end" viewBox="0 0 10 10"><path d="M1 1l4 4-4 4M5 1l4 4-4 4" fill="none" stroke="#fff" stroke-width="1"/></svg></div>
  <div class="step step--top step--fwd" style="left:292px;width:99px"><div class="two"><span>Planung Architekt</span><span>Beratung</span></div><svg class="chev chev--end" viewBox="0 0 10 10"><path d="M1 1l4 4-4 4M5 1l4 4-4 4" fill="none" stroke="#fff" stroke-width="1"/></svg></div>
  <div class="step step--top step--fwd" style="left:464px;width:114px">Angebotskalkulation<svg class="chev chev--end" viewBox="0 0 10 10"><path d="M1 1l4 4-4 4M5 1l4 4-4 4" fill="none" stroke="#fff" stroke-width="1"/></svg></div>
  <div class="step step--top step--fwd" style="left:652px;width:103px">Angebots-<br>überarbeitung<svg class="chev chev--end" viewBox="0 0 10 10"><path d="M1 1l4 4-4 4M5 1l4 4-4 4" fill="none" stroke="#fff" stroke-width="1"/></svg></div>
  <div class="step step--top step--fwd" style="left:830px;width:103px">Auftragsklärung /<br>- planung<svg class="chev chev--end" viewBox="0 0 10 10"><path d="M1 1l4 4-4 4M5 1l4 4-4 4" fill="none" stroke="#fff" stroke-width="1"/></svg></div>
  <div class="step step--top step--fwd" style="left:1008px;width:90px">Fertigungs-<br>planung<svg class="chev chev--end" viewBox="0 0 10 10"><path d="M1 1l4 4 4-4M1 5l4 4 4-4" fill="none" stroke="#fff" stroke-width="1"/></svg></div>

  <div class="dot" style="left:254px;top:80px"></div><p class="label" style="left:254px;top:98px">Auftragseingang<br>Architekt</p>
  <div class="dot" style="left:427px;top:80px"></div><p class="label" style="left:427px;top:98px">Anfrageneingang<br>Bauwerk</p>
  <div class="dot" style="left:615px;top:80px"></div><p class="label" style="left:615px;top:98px">Angebotsausgang</p>
  <div class="dot" style="left:793px;top:80px"></div><p class="label" style="left:793px;top:98px">Auftragseingang</p>
  <div class="dot" style="left:970px;top:80px"></div><p class="label" style="left:970px;top:98px">Klar-Punkt</p>
  <div class="dot" style="left:153px;top:118px"></div><p class="label" style="left:154px;top:132px">Marktrecherche<br>des Kunden</p>
  <div class="dot" style="left:153px;top:267px"></div><p class="label" style="left:154px;top:281px">Abnahme</p>

  <p class="label label--aside" style="top:127px">Beschaffungen</p>
  <div class="ok" style="left:1063px;top:132px"><svg viewBox="0 0 35 35"><path d="M11 11l5 5 9-9" fill="none" stroke="#fff" stroke-width="1.4"/><text x="17.5" y="27" fill="#fff" font-family="Jost,sans-serif" font-size="8.5" text-anchor="middle">OK</text></svg></div>

  <div class="actor actor--customer"><svg width="26" height="28" viewBox="0 0 26 28"><circle cx="13" cy="7" r="5.5" fill="none" stroke="#fff" stroke-width="1.4"/><path d="M2 27v-4a11 9 0 0 1 22 0v4" fill="none" stroke="#fff" stroke-width="1.4"/></svg><span class="name">Kunde</span><svg width="9" height="9" viewBox="0 0 10 10"><path d="M1 5l4-4 4 4M1 9l4-4 4 4" fill="none" stroke="#fff" stroke-width="1"/></svg></div>
  <div class="actor actor--supplier"><svg width="28" height="26" viewBox="0 0 28 26"><path d="M3 24V2h4v10l5-5v5l5-5v5l5-5v17H3z" fill="none" stroke="#fff" stroke-width="1.4"/></svg><span class="name">Lieferanten</span><svg width="9" height="9" viewBox="0 0 10 10"><path d="M1 1l4 4 4-4M1 5l4 4 4-4" fill="none" stroke="#fff" stroke-width="1"/></svg></div>

  <div class="step step--bottom step--back" style="left:119px;width:114px">Fremdleistungen<svg class="chev chev--start" viewBox="0 0 10 10"><path d="M1 5l4-4 4 4M1 9l4-4 4 4" fill="none" stroke="#fff" stroke-width="1"/></svg></div>
  <div class="step step--bottom step--back" style="left:239px;width:150px">Montage<svg class="chev chev--start" viewBox="0 0 10 10"><path d="M5 1L1 5l4 4M9 1L5 5l4 4" fill="none" stroke="#fff" stroke-width="1"/></svg></div>
  <div class="ok" style="left:427px;top:329px"><svg viewBox="0 0 35 35"><path d="M11 11l5 5 9-9" fill="none" stroke="#fff" stroke-width="1.4"/><text x="17.5" y="27" fill="#fff" font-family="Jost,sans-serif" font-size="8.5" text-anchor="middle">OK</text></svg></div>
  <p class="label" style="left:427px;top:352px">Montage</p>
  <div class="step step--bottom" style="left:464px;width:50px">Transport</div>
  <div class="step step--bottom" style="left:518px;width:54px">Verladung</div>
  <div class="step step--bottom" style="left:578px;width:224px"><div class="two"><span>Fremdleistungen</span><span>Werkstattproduktion</span></div><svg class="chev chev--start" viewBox="0 0 10 10"><path d="M5 1L1 5l4 4M9 1L5 5l4 4" fill="none" stroke="#fff" stroke-width="1"/></svg></div>
  <div class="ok" style="left:842px;top:329px"><svg viewBox="0 0 35 35"><path d="M11 11l5 5 9-9" fill="none" stroke="#fff" stroke-width="1.4"/><text x="17.5" y="27" fill="#fff" font-family="Jost,sans-serif" font-size="8.5" text-anchor="middle">OK</text></svg></div>
  <p class="label" style="left:842px;top:352px">Werkstatt</p>
  <div class="step step--bottom" style="left:881px;width:217px">Materiallieferungen<svg class="chev chev--start" viewBox="0 0 10 10"><path d="M5 1L1 5l4 4M9 1L5 5l4 4" fill="none" stroke="#fff" stroke-width="1"/></svg></div>
</section>

<div class="brand">
  <div class="rule"></div>
  <div class="mark"><span class="square"></span><span class="name">LINDTAL HOLZHAUS</span></div>
</div>

<section class="flow flow--alt">
  <div class="step step--top step--fwd" style="left:119px;width:99px">Marketing<svg class="chev chev--end" viewBox="0 0 10 10"><path d="M1 1l4 4-4 4M5 1l4 4-4 4" fill="none" stroke="#fff" stroke-width="1"/></svg></div>
  <div class="step step--top step--fwd" style="left:292px;width:99px"><div class="two"><span>Planung Architekt</span><span>Beratung</span></div><svg class="chev chev--end" viewBox="0 0 10 10"><path d="M1 1l4 4-4 4M5 1l4 4-4 4" fill="none" stroke="#fff" stroke-width="1"/></svg></div>
  <div class="step step--top step--fwd" style="left:464px;width:114px">Angebotskalkulation<svg class="chev chev--end" viewBox="0 0 10 10"><path d="M1 1l4 4-4 4M5 1l4 4-4 4" fill="none" stroke="#fff" stroke-width="1"/></svg></div>
  <div class="step step--top step--fwd" style="left:652px;width:103px">Angebots-<br>überarbeitung<svg class="chev chev--end" viewBox="0 0 10 10"><path d="M1 1l4 4-4 4M5 1l4 4-4 4" fill="none" stroke="#fff" stroke-width="1"/></svg></div>
  <div class="step step--top step--fwd" style="left:830px;width:103px">Auftragsklärung /<br>- planung<svg class="chev chev--end" viewBox="0 0 10 10"><path d="M1 1l4 4-4 4M5 1l4 4-4 4" fill="none" stroke="#fff" stroke-width="1"/></svg></div>
  <div class="step step--top step--fwd" style="left:1008px;width:90px">Fertigungs-<br>planung<svg class="chev chev--end" viewBox="0 0 10 10"><path d="M1 1l4 4 4-4M1 5l4 4 4-4" fill="none" stroke="#fff" stroke-width="1"/></svg></div>

  <div class="dot" style="left:254px;top:80px"></div><p class="label" style="left:254px;top:98px">Auftragseingang<br>Architekt</p>
  <div class="dot" style="left:427px;top:80px"></div><p class="label" style="left:427px;top:98px">Anfrageneingang<br>Bauwerk</p>
  <div class="dot" style="left:615px;top:80px"></div><p class="label" style="left:615px;top:98px">Angebotsausgang</p>
  <div class="dot" style="left:793px;top:80px"></div><p class="label" style="left:793px;top:98px">Auftragseingang</p>
  <div class="dot" style="left:970px;top:80px"></div><p class="label" style="left:970px;top:98px">Klar-Punkt</p>
  <div class="dot" style="left:153px;top:118px"></div><p class="label" style="left:154px;top:132px">Marktrecherche<br>des Kunden</p>
  <div class="dot" style="left:153px;top:267px"></div><p class="label" style="left:154px;top:281px">Abnahme</p>

  <p class="label label--aside" style="top:127px">Beschaffungen</p>
  <div class="ok" style="left:1063px;top:132px"><svg viewBox="0 0 35 35"><path d="M11 11l5 5 9-9" fill="none" stroke="#fff" stroke-width="1.4"/><text x="17.5" y="27" fill="#fff" font-family="Jost,sans-serif" font-size="8.5" text-anchor="middle">OK</text></svg></div>

  <div class="actor actor--customer"><svg width="26" height="28" viewBox="0 0 26 28"><circle cx="13" cy="7" r="5.5" fill="none" stroke="#fff" stroke-width="1.4"/><path d="M2 27v-4a11 9 0 0 1 22 0v4" fill="none" stroke="#fff" stroke-width="1.4"/></svg><span class="name">Kunde</span><svg width="9" height="9" viewBox="0 0 10 10"><path d="M1 5l4-4 4 4M1 9l4-4 4 4" fill="none" stroke="#fff" stroke-width="1"/></svg></div>
  <div class="actor actor--supplier"><svg width="28" height="26" viewBox="0 0 28 26"><path d="M3 24V2h4v10l5-5v5l5-5v5l5-5v17H3z" fill="none" stroke="#fff" stroke-width="1.4"/></svg><span class="name">Lieferanten</span><svg width="9" height="9" viewBox="0 0 10 10"><path d="M1 1l4 4 4-4M1 5l4 4 4-4" fill="none" stroke="#fff" stroke-width="1"/></svg></div>

  <div class="step step--bottom step--back" style="left:119px;width:114px">Fremdleistungen<svg class="chev chev--start" viewBox="0 0 10 10"><path d="M1 5l4-4 4 4M1 9l4-4 4 4" fill="none" stroke="#fff" stroke-width="1"/></svg></div>
  <div class="step step--bottom step--back" style="left:239px;width:150px">Montage<svg class="chev chev--start" viewBox="0 0 10 10"><path d="M5 1L1 5l4 4M9 1L5 5l4 4" fill="none" stroke="#fff" stroke-width="1"/></svg></div>
  <div class="ok" style="left:427px;top:329px"><svg viewBox="0 0 35 35"><path d="M11 11l5 5 9-9" fill="none" stroke="#fff" stroke-width="1.4"/><text x="17.5" y="27" fill="#fff" font-family="Jost,sans-serif" font-size="8.5" text-anchor="middle">OK</text></svg></div>
  <p class="label" style="left:427px;top:352px">Montage</p>
  <div class="step step--bottom" style="left:464px;width:50px">Transport</div>
  <div class="step step--bottom" style="left:518px;width:54px">Verladung</div>
  <div class="step step--bottom" style="left:578px;width:224px"><div class="two"><span>Fremdleistungen</span><span>Werkstattproduktion</span></div><svg class="chev chev--start" viewBox="0 0 10 10"><path d="M5 1L1 5l4 4M9 1L5 5l4 4" fill="none" stroke="#fff" stroke-width="1"/></svg></div>
  <div class="ok" style="left:842px;top:329px"><svg viewBox="0 0 35 35"><path d="M11 11l5 5 9-9" fill="none" stroke="#fff" stroke-width="1.4"/><text x="17.5" y="27" fill="#fff" font-family="Jost,sans-serif" font-size="8.5" text-anchor="middle">OK</text></svg></div>
  <p class="label" style="left:842px;top:352px">Werkstatt</p>
  <div class="step step--bottom" style="left:881px;width:217px">Materiallieferungen<svg class="chev chev--start" viewBox="0 0 10 10"><path d="M5 1L1 5l4 4M9 1L5 5l4 4" fill="none" stroke="#fff" stroke-width="1"/></svg></div>
</section>

</body>
</html>
```